Community Manager Proposal for the Varnell Brand in Colombia and Another for the Kemra Brand

I have a powerpoint presentation (attached), but I need to enhance it with a very cool template, one with the Varnell brand (mostly yellow please - you can get logos online) and another for the Kemra brand (blue - you can get logos online) include images and cool movement and dynamics to the presentation. The information is in spanish, but I can enter it or modify it when you give me the final template. The proposal is for the exclusive Varnell tire importer and Kemra importer for Colombia, South America regarding social network management. They are Distribuidora Central de Rodados BRESO SAS (www.breso-example.com and www.varnellcolombia-example.com and www.kemracolombia-example.com) and they manage auto, 4x4, truck and motorcycle tires so that you can enhance the powerpoint presentation with related images. The final result is two presentations with the same information, but one for Varnell brand and the other for the Kemra brand.

```html
<!DOCTYPE html>
<html lang="es">
<head>
<meta charset="utf-8">
<title>Varnell · Propuesta Community Manager</title>
<link href="https://fonts.googleapis.com/css2?family=Questrial&display=swap" rel="stylesheet">
<style>
  :root{
    --page:#ececec;
    --slide:#f7f7f7;
    --ink:#1e1e1e;
    --black:#121212;
    --yellow:#f7dc0a;
    --tire:#d9d9d9;
    --bullet:#c9a800;
    --mark-blue:#3b6fb6;
    --mark-red:#c0392b;
    --brand-dot:#c00;
  }
  *{margin:0;padding:0;box-sizing:border-box}
  html,body{width:1200px;height:1000px;overflow:hidden}
  body{
    background:var(--page);
    background-image:repeating-linear-gradient(45deg,rgba(0,0,0,.025) 0 2px,transparent 2px 6px);
    font-family:"Questrial",sans-serif;color:var(--ink);position:relative;
  }
  .slide{
    position:absolute;left:303px;width:610px;height:455px;overflow:hidden;
    background:linear-gradient(180deg,#fff 0%,var(--slide) 60%,#ececec 100%);
    box-shadow:2px 3px 5px rgba(0,0,0,.35);
  }
  .slide--plan{top:32px}
  .slide--media{top:518px}
  .slide__header{position:absolute;left:0;top:0;width:610px;height:80px}
  .social-collage{position:absolute;left:0;top:0;width:320px;height:70px;
    background:linear-gradient(90deg,var(--black) 0%,#2a2a2a 55%,var(--yellow) 100%)}
  .tire-visual{position:absolute;left:0;top:70px;width:150px;height:310px;
    background:linear-gradient(90deg,var(--tire) 0%,rgba(230,230,230,.6) 60%,rgba(255,255,255,0) 100%)}
  .slide__title{
    position:absolute;top:33px;height:45px;background:var(--black);color:#fff;
    font-size:27px;font-weight:400;letter-spacing:1.5px;line-height:45px;text-align:center;white-space:nowrap;
    border:1px solid #555;box-shadow:2px 2px 3px rgba(0,0,0,.4);
  }
  .slide--plan .slide__title{left:42px;width:522px}
  .slide--media .slide__title{left:180px;width:262px}
  .bullets{position:absolute;left:42px;list-style:none;font-size:20px;letter-spacing:.9px}
  .bullets li{position:relative;padding-left:18px;height:29px;line-height:29px;white-space:nowrap}
  .bullets li::before{content:"";position:absolute;left:0;top:8px;width:9px;height:11px;
    border-radius:50%;background:radial-gradient(circle at 40% 35%,var(--yellow) 0 35%,var(--bullet) 40%,#222 80%)}
  .bullets li.sub{margin-left:28px}
  .bullets li.gap{margin-top:29px}
  .slide--plan .bullets,.slide--media .bullets{top:108px}
  .channel{display:inline-block;width:118px}
  .channel-mark{display:inline-block;width:15px;height:15px;border-radius:50%;background:var(--mark-blue);vertical-align:middle;margin-left:6px}
  .channel-mark--video{background:var(--mark-red)}
  .note{position:absolute;left:40px;top:287px;font-size:20px;letter-spacing:.9px;line-height:24px;white-space:nowrap}
  .slide__footer{position:absolute;left:0;top:378px;width:610px;height:77px}
  .footer-band{position:absolute;left:0;top:0;width:610px;height:14px;background:var(--black)}
  .footer-yellow{position:absolute;left:0;top:14px;width:610px;height:48px;
    background:linear-gradient(90deg,#ddd 0%,#bbb 20%,var(--yellow) 42%,var(--yellow) 100%)}
  .car-visual{position:absolute;left:0;top:14px;width:200px;height:63px;
    background:linear-gradient(90deg,#e8e8e8 0%,#555 45%,rgba(80,80,80,0) 100%)}
  .footer-base{position:absolute;left:0;top:62px;width:610px;height:15px;background:var(--black)}
  .brand{position:absolute;right:28px;top:26px;font-size:18px;color:var(--black);display:flex;align-items:center;gap:6px;letter-spacing:1px}
  .brand__dot{width:14px;height:14px;border-radius:50%;background:var(--brand-dot)}
  .slogan{position:absolute;right:12px;top:63px;font-size:10px;color:var(--yellow);letter-spacing:.8px;line-height:13px}
</style>
</head>
<body>

<section class="slide slide--plan">
  <div class="tire-visual" role="img" aria-label="Llanta todoterreno en tono gris claro como fondo"></div>
  <div class="slide__header">
    <svg width="610" height="80" viewBox="0 0 610 80">
      <polygon points="300,0 610,0 610,10 300,30" fill="#f7dc0a"/>
      <polygon points="300,30 610,10 610,20 300,44" fill="#121212"/>
    </svg>
    <div class="social-collage" role="img" aria-label="Collage de iconos de redes sociales en negro y amarillo"></div>
    <h1 class="slide__title">Tiempos, Proyecciones &amp; Aspiraciones</h1>
  </div>
  <ul class="bullets">
    <li>Apoyo de forma permanente.</li>
    <li>Crecimiento de usuarios en cada medio. 6 meses.</li>
    <li class="sub">Murolink. 500 Personas.</li>
    <li class="sub">Profesia. 100 Contactos.</li>
    <li class="sub">Piador. 500 Seguidores.</li>
    <li class="sub">Fotogram. 500 Seguidores.</li>
    <li class="gap">Busqueda de un crecimiento sostenido del target.</li>
  </ul>
  <div class="slide__footer">
    <div class="footer-band"></div>
    <div class="footer-yellow"></div>
    <div class="car-visual" role="img" aria-label="Vehículo blanco con rin oscuro"></div>
    <div class="footer-base"></div>
    <div class="brand"><span class="brand__dot"></span>VARNELL</div>
    <div class="slogan">DRIVE WITH TRUST</div>
  </div>
</section>

<section class="slide slide--media">
  <div class="tire-visual" role="img" aria-label="Llanta todoterreno en tono gris claro como fondo"></div>
  <div class="slide__header">
    <svg width="610" height="80" viewBox="0 0 610 80">
      <polygon points="300,0 610,0 610,10 300,30" fill="#f7dc0a"/>
      <polygon points="300,30 610,10 610,20 300,44" fill="#121212"/>
    </svg>
    <div class="social-collage" role="img" aria-label="Collage de iconos de redes sociales en negro y amarillo"></div>
    <h1 class="slide__title">Medios</h1>
  </div>
  <ul class="bullets">
    <li><span class="channel">Murolink.</span><span class="channel-mark"></span></li>
    <li><span class="channel">Profesia.</span><span class="channel-mark"></span></li>
    <li><span class="channel">Piador.</span><span class="channel-mark"></span></li>
    <li><span class="channel">Videora.</span><span class="channel-mark channel-mark--video"></span></li>
    <li><span class="channel">Fotogram.</span><span class="channel-mark"></span></li>
  </ul>
  <p class="note">(Detallar objetivos y plan por cada medio.<br>Investigacion inicial de marca en medios,<br>elaboracion de contenidos, ideas de rifas y material, )</p>
  <div class="slide__footer">
    <div class="footer-band"></div>
    <div class="footer-yellow"></div>
    <div class="car-visual" role="img" aria-label="Vehículo blanco con rin oscuro"></div>
    <div class="footer-base"></div>
    <div class="brand"><span class="brand__dot"></span>VARNELL</div>
    <div class="slogan">DRIVE WITH TRUST</div>
  </div>
</section>

</body>
</html>
```